Redesign Business Cards, Attached

Please read instructions carefully. If you have any questions send a message before submitting your ONE design. Please redesign attached business cards. Double sided. Use same content and descriptions. Use black, silver, crimson red and gold colors. My only issue with the attached design is the background colors. I like the layout as-is. I can provide the individual pictures on the back side later. Do not submit more than one design. One submission shall include both front and back. Do not submit front and back separately. A second project will be launched to create a matching post card after completion of this.
Industry/Entity Type
see description and attachments.
Contact Information for Business Card
Requirements
Must have
- see description and attachments.
Nice to have
Should not have

```html
<!DOCTYPE html>
<html lang="en">
<head>
<meta charset="utf-8">
<title>Helm Ready – Business Card</title>
<link rel="stylesheet" href="https://fonts.googleapis.com/css2?family=Montserrat:ital,wght@0,400;0,500;0,600;1,600;1,700&display=swap">
<style>
  :root {
    --page: #a9a7a8;
    --gold: #d0a52a;
    --gold-light: #dcb13a;
    --silver: #c3c7cc;
    --silver-light: #e4e7ea;
    --silver-dark: #8e949b;
    --crimson: #a3162b;
    --ink: #262626;
    --ink-soft: #3a3a3a;
    --white: #ffffff;
  }
  * { box-sizing: border-box; margin: 0; padding: 0; }
  html, body { width: 1200px; height: 1200px; overflow: hidden; }
  body {
    background: var(--page);
    font-family: "Montserrat", Arial, sans-serif;
    position: relative;
  }
  .card {
    position: absolute;
    left: 166px;
    width: 869px;
    height: 506px;
    overflow: hidden;
  }
  .card--front { top: 69px; background: var(--gold); }
  .card--back { top: 625px; background: var(--ink); }

  .front-photo {
    position: absolute; inset: 0;
    background: linear-gradient(90deg, var(--gold) 0%, var(--gold) 42%, var(--gold-light) 52%, var(--silver-dark) 68%, var(--silver) 82%, var(--silver-light) 100%);
  }
  .back-photo {
    position: absolute; inset: 0;
    background: radial-gradient(ellipse at 30% 35%, var(--ink-soft) 0%, var(--ink) 65%);
  }
  .accent-rule {
    position: absolute; left: 0; right: 0; bottom: 0;
    height: 6px; background: var(--crimson);
  }

  .brand-mark {
    position: absolute;
    width: 176px; height: 176px;
    border-radius: 50%;
    background: var(--ink);
    border: 5px solid var(--silver);
    display: flex; align-items: center; justify-content: center;
    text-align: center;
    color: var(--white);
    font-weight: 600;
    font-size: 22px;
    line-height: 1.15;
    letter-spacing: 1px;
  }
  .card--front .brand-mark { left: 637px; top: 58px; }
  .card--back .brand-mark { left: 346px; top: 49px; }

  .identity { position: absolute; left: 60px; top: 132px; color: var(--white); }
  .identity__name { font-size: 37px; font-weight: 600; letter-spacing: .3px; }
  .identity__role { font-size: 22px; font-weight: 400; line-height: 29px; margin-top: 6px; }

  .contact { position: absolute; left: 60px; top: 281px; list-style: none; color: var(--white); }
  .contact li { display: flex; align-items: center; gap: 16px; font-size: 22px; height: 33px; }
  .contact svg { width: 16px; height: 16px; fill: var(--white); flex: none; }

  .services {
    position: absolute; left: 51px; top: 239px;
    display: grid;
    grid-template-columns: repeat(4, 181px);
    grid-auto-rows: 82px;
    column-gap: 16px; row-gap: 18px;
    list-style: none;
  }
  .service {
    background: var(--gold);
    border-radius: 22px 4px 22px 4px;
    border-bottom: 3px solid var(--crimson);
    color: var(--white);
    font-style: italic; font-weight: 600;
    font-size: 15px; line-height: 19px;
    padding: 18px 8px 0 22px;
    white-space: nowrap;
  }
  .web {
    position: absolute; left: 0; right: 0; top: 440px;
    text-align: center; color: var(--white);
    font-size: 25px; font-weight: 600; letter-spacing: .3px;
  }
</style>
</head>
<body>
  <section class="card card--front">
    <div class="front-photo" role="img" aria-label="Photo of a white centre-console boat cruising across sunlit water"></div>
    <div class="brand-mark">HELM<br>READY</div>
    <div class="identity">
      <h1 class="identity__name">Dana R. Wexley</h1>
      <p class="identity__role">USCG Licensed Captain<br>Certified Instructor</p>
    </div>
    <ul class="contact">
      <li><svg viewBox="0 0 24 24"><path d="M6.6 10.8a15.1 15.1 0 0 0 6.6 6.6l2.2-2.2c.3-.3.7-.4 1-.2 1.1.4 2.3.6 3.6.6.6 0 1 .4 1 1V20c0 .6-.4 1-1 1A17 17 0 0 1 3 4c0-.6.4-1 1-1h3.5c.6 0 1 .4 1 1 0 1.3.2 2.5.6 3.6.1.3 0 .7-.2 1z"/></svg>(727) 555-0148</li>
      <li><svg viewBox="0 0 24 24"><path d="M2 5h20v14H2zm2 2v.5l8 5 8-5V7l-8 5z"/></svg>hello@helmready.com</li>
      <li><svg viewBox="0 0 24 24"><path d="M12 2a10 10 0 1 0 0 20 10 10 0 0 0 0-20zm6.9 6h-3a15.7 15.7 0 0 0-1.4-3.6A8 8 0 0 1 18.9 8zM12 4c.8 1.2 1.5 2.5 1.9 4h-3.8c.4-1.5 1.1-2.8 1.9-4zM4.3 14a8 8 0 0 1 0-4h3.4a16.5 16.5 0 0 0 0 4zm.8 2h3a15.7 15.7 0 0 0 1.4 3.6A8 8 0 0 1 5.1 16zm3-8h-3a8 8 0 0 1 4.4-3.6C8.9 5.6 8.4 6.8 8.1 8zM12 20c-.8-1.2-1.5-2.5-1.9-4h3.8c-.4 1.5-1.1 2.8-1.9 4zm2.3-6H9.7a14.7 14.7 0 0 1 0-4h4.6a14.7 14.7 0 0 1 0 4zm.2 5.6c.6-1.1 1.1-2.3 1.4-3.6h3a8 8 0 0 1-4.4 3.6zm1.8-5.6a16.5 16.5 0 0 0 0-4h3.4a8 8 0 0 1 0 4z"/></svg>www.HelmReady.com</li>
    </ul>
    <div class="accent-rule"></div>
  </section>

  <section class="card card--back">
    <div class="back-photo" role="img" aria-label="Darkened photo of a boat underway on open water"></div>
    <div class="brand-mark">HELM<br>READY</div>
    <ul class="services">
      <li class="service">Hands-on<br>Boat Training</li>
      <li class="service">Introduction<br>to Power Boating</li>
      <li class="service">Precision Docking<br>&amp; Boat Handling</li>
      <li class="service">Open Water<br>Boat Handling</li>
      <li class="service">Island<br>Anchoring</li>
      <li class="service">Open Water<br>Advanced<br>Maneuvers</li>
      <li class="service">Coastal<br>Navigation</li>
      <li class="service">Captaining /<br>Piloting Service<br>for Your Outings</li>
    </ul>
    <p class="web">www.HelmReady.com</p>
    <div class="accent-rule"></div>
  </section>
</body>
</html>
```